I want to sell a virtual ticket that captures customers details.

Using this information, i manually write the customers details on a piece of paper and enter them into a draw/raffle to potentially win a watch. I dont need random generators/software to pick winners, as law mandates this process to be physically done. All i need is a nice website that allows customers to purchase and enter. I have posted a few links below in the description. If you refer to orvanteltrading.com, you will see what i am after. I have my own site www.thekestrelmarque.com.au but i dont like how it looks and i want something better. I hope this will give you an idea on what i am after.

Target Market(s)

adults aged approximately 24-56

Industry/Entity Type

luxury watches / contestant giveaways

Number of Pages Required

4 page

Font styles to use
Serif
Other font styles liked:
• something classy - i am not sure

Colors

Designer to choose only greyscale colors for use in the design.

Requirements
Must have
• Stripe payment software

```html
<!DOCTYPE html>
<html lang="en">
<head>
<meta charset="utf-8">
<title>The Kestrel Marque</title>
<link rel="stylesheet" href="https://fonts.googleapis.com/css2?family=Oswald:wght@400;500&family=Lato:wght@400;700&display=swap">
<style>
:root{
  --ink:#111;
  --text:#333;
  --navy:#23264a;
  --heading:#3b3f6b;
  --mist:#f3f3f3;
  --white:#fff;
  --divider:#3a3d60;
}
*{box-sizing:border-box;margin:0;padding:0}
html,body{width:1200px;height:2310px;overflow:hidden}
body{background:var(--white);font-family:'Lato',sans-serif;color:var(--text);position:relative}
.page{position:relative;width:1200px;height:2310px}

/* hero */
.hero{position:absolute;left:0;top:0;width:1200px;height:729px;background:var(--mist)}
.ticket-link{position:absolute;left:75px;top:52px;font-size:14px;color:var(--text);text-decoration:underline}
.brand{position:absolute;left:0;width:1200px;top:46px;text-align:center;font-family:'Oswald',sans-serif;font-weight:500;font-size:28px;letter-spacing:.5px;color:var(--ink)}
.menu{position:absolute;left:1104px;top:54px;width:22px}
.hero-photo{position:absolute;left:342px;top:119px;width:784px;height:537px;background:linear-gradient(135deg,#d9dcdc 0%,#b9bcbc 40%,#c9a968 55%,#9ea3a6 75%,#dfe2e2 100%)}
.hero-title{position:absolute;left:75px;top:188px;width:420px;font-family:'Oswald',sans-serif;font-weight:400;font-size:44px;line-height:50px;color:var(--ink)}
.countdown{position:absolute;left:75px;top:400px;height:92px;display:flex;background:var(--navy);color:var(--white)}
.countdown .unit{height:92px;display:flex;flex-direction:column;align-items:center;justify-content:center;border-right:1px solid var(--divider)}
.countdown .unit:last-child{border-right:0}
.countdown .num{font-size:33px;line-height:36px}
.countdown .lbl{font-size:14px}
.promo{position:absolute;left:75px;top:492px;width:422px;height:164px;background:var(--white);padding:16px 0 0 23px}
.promo p{font-family:'Oswald',sans-serif;font-size:31px;line-height:40px;color:var(--ink)}
.promo a{display:inline-block;margin-top:6px;font-family:'Oswald',sans-serif;font-size:24px;color:var(--navy);text-decoration:underline}

/* shared headings */
.section-title{font-size:43px;font-weight:400;color:var(--heading)}

/* packages */
.packages{position:absolute;left:0;top:729px;width:1200px;height:326px;background:var(--white)}
.packages .section-title{position:absolute;left:75px;top:56px}
.package{position:absolute;top:150px;width:340px}
.price{font-size:43px;font-weight:700;color:var(--ink);line-height:48px}
.price sup{font-size:20px;vertical-align:top;position:relative;top:4px}
.package p{font-size:18px;line-height:31px;color:var(--text);margin-top:4px}

/* who we are */
.who{position:absolute;left:0;top:1055px;width:1200px;height:382px;background:var(--mist)}
.who .section-title{position:absolute;left:75px;top:87px}
.who p{position:absolute;left:75px;top:170px;width:640px;font-size:26px;line-height:41.5px;color:var(--text)}
.who-photo{position:absolute;left:792px;top:22px;width:276px;height:340px;border-radius:46% 40% 44% 40%;background:radial-gradient(circle at 40% 40%,#3a3a3a 0%,#5c5c5c 35%,#a3a3a3 60%,#e4e4e4 90%)}

/* how to play */
.how{position:absolute;left:0;top:1437px;width:1200px;height:308px;background:var(--white)}
.how .section-title{position:absolute;left:0;width:1200px;text-align:center;top:52px}
.step{position:absolute;top:152px;display:flex}
.step svg{margin-right:22px;flex:none}
.step h3{font-size:26px;font-weight:700;color:var(--ink);line-height:30px}
.step p{font-size:19px;margin-top:20px;color:var(--text)}

/* about */
.about{position:absolute;left:0;top:1745px;width:1200px;height:383px;background:var(--mist)}
.about .section-title{position:absolute;left:75px;top:68px}
.about .col{position:absolute;top:140px;width:512px;font-size:16.5px;line-height:28.6px;color:var(--text)}

/* footer */
.footer{position:absolute;left:0;top:2128px;width:1200px;height:182px;background:var(--white)}
.footer nav{position:absolute;top:40px;left:0;width:1200px;display:flex;justify-content:center;gap:52px;font-size:19px;color:var(--text)}
.legal{position:absolute;top:83px;left:0;width:1200px;text-align:center;font-size:13px;color:var(--text)}
.legal u{color:var(--ink)}
.social{position:absolute;top:116px;left:0;width:1200px;display:flex;justify-content:center;gap:22px}
.social span{width:20px;height:20px;border-radius:50%;background:var(--text)}
</style>
</head>
<body>
<div class="page">

<header class="hero">
  <a class="ticket-link">Get your Virtaul Ticket</a>
  <div class="brand">THE KESTREL MARQUE</div>
  <svg class="menu" viewBox="0 0 22 18" height="18"><path d="M0 1h22M0 9h22M0 17h22" stroke="#222" stroke-width="2"/></svg>
  <div class="hero-photo" role="img" aria-label="Photo of several luxury wristwatches with steel and gold bracelets"></div>
  <h1 class="hero-title">Sed ut perspiciatis unde omnis iste natus error sit voluptatem</h1>
  <div class="countdown">
    <div class="unit" style="width:81px"><span class="num">0</span><span class="lbl">Days</span></div>
    <div class="unit" style="width:85px"><span class="num">6</span><span class="lbl">Hours</span></div>
    <div class="unit" style="width:85px"><span class="num">25</span><span class="lbl">Mintues</span></div>
    <div class="unit" style="width:86px"><span class="num">56</span><span class="lbl">Seconds</span></div>
  </div>
  <div class="promo">
    <p>Nemo enim ipsam voluptatem quia voluptas sit</p>
    <a>Subscribe Now</a>
  </div>
</header>

<section class="packages">
  <h2 class="section-title">Membership Packages</h2>
  <div class="package" style="left:76px"><div class="price"><sup>$</sup>6.99</div><p>Buys you a membership + one entry to the Corvane</p></div>
  <div class="package" style="left:434px"><div class="price"><sup>$</sup>10.99</div><p>Buys you a membership + two entries to the Corvane</p></div>
  <div class="package" style="left:794px"><div class="price"><sup>$</sup>15.00</div><p>Buys you a membership + three entry to the Corvane</p></div>
</section>

<section class="who">
  <h2 class="section-title">Who We Are</h2>
  <p>A 100% Australian owned company whose main goal is to create a community for people who love what we love –&nbsp; luxury watches.</p>
  <div class="who-photo" role="img" aria-label="Photo of a steel chronograph wristwatch with a black dial"></div>
</section>

<section class="how">
  <h2 class="section-title">How to Play</h2>
  <div class="step" style="left:78px">
    <svg width="56" height="50" viewBox="0 0 56 50" fill="#3b3f6b"><path d="M28 2l12 6v12l-12 6-12-6V8z"/><path d="M14 24l12 6v12l-12 6-12-6V30z"/><path d="M42 24l12 6v12l-12 6-12-6V30z"/></svg>
    <div><h3>Step 1</h3><p>Pick a package.</p></div>
  </div>
  <div class="step" style="left:434px">
    <svg width="56" height="56" viewBox="0 0 56 56" fill="#3b3f6b"><path d="M2 0h28l14 14v42H2z"/><path d="M10 30h26M10 38h26M10 46h26" stroke="#fff" stroke-width="3"/></svg>
    <div><h3>Step 2</h3><p>Enter Details.</p></div>
  </div>
  <div class="step" style="left:783px">
    <svg width="56" height="52" viewBox="0 0 56 52" fill="#3b3f6b"><path d="M28 14c-4-10-16-14-18-6-1 4 4 6 18 6zM28 14c4-10 16-14 18-6 1 4-4 6-18 6z"/><rect x="0" y="14" width="56" height="12" rx="2"/><rect x="4" y="28" width="48" height="24" rx="2"/><rect x="24" y="14" width="8" height="38" fill="#fff"/></svg>
    <div><h3>Step 3</h3><p>Wait for draw – its that simple!</p></div>
  </div>
</section>

<section class="about">
  <h2 class="section-title">About Us</h2>
  <p class="col" style="left:75px">We are a group of friends from Melbourne, Australia, who all share a common passion – a love for watches. We aim to provide an equal opportunity for all watch lovers in Australia, whilst, more importantly, paving the way for a cleaner, eco-friendlier world. We strongly believe that all communities, regardless of interests, should share a common goal, which is why we have joinedforces</p>
  <p class="col" style="left:617px">with (TO BE CONFIRMED), whose main aim is to help plant trees across Australia to prevent deforestation in our own backyard. Our services are one of a kind, as each package sold goes towards planting trees in the much-needed regions of Australia. We hope you are excited as we are as we embark on this journey together!</p>
</section>

<footer class="footer">
  <nav><a>Home</a><a>Who We Are</a><a>How to Play</a><a>About Us</a><a>Contact Us</a></nav>
  <p class="legal">Copyright © 2021. Company Name - All rights reserved. Terms And Conditions. <u>Disclaimer</u></p>
  <div class="social" aria-label="Social links"><span></span><span></span><span></span><span></span><span></span></div>
</footer>

</div>
</body>
</html>
```